Fox & Fig honey company needs a label design.

We need a label design for a new honey company, based in the state of Florida called 'Fox & Fig". We are supplying our online customers with the highest quality of the various kinds of raw honey. Our product is honey in the oval hexagon glass jar with black lid. We would like to see designs that use black background with gold font .
In the upper part of the label is gold flying Honey Bee (profile, silhouette). The name of the brand "Fox & Fig" - Caramel font. Additional fonts are Cinzel, Source Sans Pro. Label measurements 2.6" by 3".
Label content:
Fox & Fig
RAW HONEY
wildflower
PURE & NATURAL
made by Florida Bees
foxandfigjars.com
NET WT 12oz (340g)

The final design should have eye catching, luxurious look.
Updates

Need extra days to review

Target Market(s)

Luxury

Industry/Entity Type

Food (bee products)

Font styles to use
Other font styles liked:
• caramel

Colors

Designer to choose colors to be used in the design.

Requirements
Must have
• Gold letters on black background, Drawing of a bee, flying in profile

```html
<!DOCTYPE html>
<html lang="en">
<head>
<meta charset="utf-8">
<title>Fox &amp; Fig — Raw Honey Label</title>
<link rel="stylesheet" href="https://fonts.googleapis.com/css2?family=Caramel&family=Source+Sans+3:wght@400;500;600&display=swap">
<style>
  :root {
    --backdrop: #f1e4d4;
    --label-black: #0b0b0b;
    --label-charcoal: #1c1c1c;
    --gold-light: #f2cf6a;
    --gold-mid: #c99526;
    --gold-deep: #8a5a10;
    --comb-tone: rgba(201, 149, 38, 0.22);
  }
  html, body {
    margin: 0;
    width: 996px;
    height: 1200px;
    overflow: hidden;
    background: var(--backdrop);
  }
  .label {
    position: absolute;
    left: 48px;
    top: 300px;
    width: 900px;
    height: 600px;
    background: radial-gradient(ellipse at 50% 45%, var(--label-charcoal) 0%, var(--label-black) 70%);
    overflow: hidden;
  }
  .comb-edge {
    position: absolute;
    top: 0;
    bottom: 0;
    width: 110px;
  }
  .comb-edge--left {
    left: 0;
    background: linear-gradient(to right, var(--comb-tone), rgba(201,149,38,0));
  }
  .comb-edge--right {
    right: 0;
    background: linear-gradient(to left, var(--comb-tone), rgba(201,149,38,0));
  }
  .gold-text {
    position: absolute;
    left: 0;
    right: 0;
    margin: 0;
    text-align: center;
    line-height: 1;
    white-space: nowrap;
    color: var(--gold-mid);
    background: linear-gradient(100deg, var(--gold-deep) 0%, var(--gold-light) 40%, var(--gold-mid) 65%, var(--gold-deep) 100%);
    -webkit-background-clip: text;
    background-clip: text;
    -webkit-text-fill-color: transparent;
  }
  .brand-name {
    top: 12px;
    font-family: "Caramel", cursive;
    font-size: 104px;
  }
  .bee-figure {
    position: absolute;
    left: 371px;
    top: 121px;
    width: 158px;
    height: 119px;
    border-radius: 50%;
    background: radial-gradient(ellipse at 50% 55%, #b8862a 0%, #6a4a14 45%, rgba(11,11,11,0) 72%);
  }
  .product-type {
    top: 258px;
    font-family: "Source Sans 3", sans-serif;
    font-weight: 500;
    font-size: 50px;
    letter-spacing: 5px;
  }
  .variety {
    top: 320px;
    font-family: "Source Sans 3", sans-serif;
    font-weight: 500;
    font-size: 44px;
    letter-spacing: 1px;
  }
  .claim {
    top: 402px;
    font-family: "Source Sans 3", sans-serif;
    font-weight: 500;
    font-size: 53px;
  }
  .website {
    top: 466px;
    font-family: "Source Sans 3", sans-serif;
    font-size: 34px;
  }
  .origin {
    top: 510px;
    font-family: "Source Sans 3", sans-serif;
    font-size: 28px;
    padding-left: 16px;
  }
  .net-weight {
    top: 561px;
    font-family: "Source Sans 3", sans-serif;
    font-size: 24px;
    padding-left: 4px;
  }
</style>
</head>
<body>
  <section class="label">
    <div class="comb-edge comb-edge--left" role="img" aria-label="Gold honeycomb pattern along the left edge"></div>
    <div class="comb-edge comb-edge--right" role="img" aria-label="Gold honeycomb pattern along the right edge"></div>

    <h1 class="gold-text brand-name">Fox &amp; Fig</h1>
    <div class="bee-figure" role="img" aria-label="Illustration of a golden honey bee in flight, shown in profile"></div>
    <p class="gold-text product-type">RAW HONEY</p>
    <p class="gold-text variety">wildflower</p>
    <p class="gold-text claim">PURE &amp; NATURAL</p>
    <p class="gold-text website">foxandfigjars.com</p>
    <p class="gold-text origin">Made by Florida Bees</p>
    <p class="gold-text net-weight">NET WT 12oz (340g)</p>
  </section>
</body>
</html>
```